Create Lanternfield HR Business Cards.

Create Business Cards for Lanternfield HR. 2 sided and Would like the back to have the logo.

Info for Business Card:
Address: 4827 Millbrook Ave Suite 230 Cleveland, Ohio 44987
Office Number: 216-555-0143
Mobile: 216-555-0192

Website: www.lanternfieldhr.example

Target Market(s)

Small to medium size businesses

Industry/Entity Type

Human Resources

Contact Information for Business Card

Company logo and information

Font styles to use
Serif
Sans Serif

Requirements
Must have
• Info for Business Card: Address: 4827 Millbrook Ave Suite 230 Cleveland, Ohio 44987 Office Number: 216-555-0143 Mobile: 216-555-0192 Website: www.lanternfieldhr.example

```html
<!DOCTYPE html>
<html lang="en">
<head>
<meta charset="utf-8">
<title>Lanternfield HR Business Cards</title>
<link rel="stylesheet" href="https://fonts.googleapis.com/css2?family=Arimo:wght@400;700&display=swap">
<style>
  :root {
    --navy: #2a2466;
    --orange: #f38b20;
    --white: #ffffff;
    --stage: #e9e9ec;
    --ink: #2a2466;
  }
  * { box-sizing: border-box; margin: 0; padding: 0; }
  html, body { width: 1200px; height: 801px; overflow: hidden; }
  body {
    background: var(--stage);
    font-family: "Arimo", Arial, sans-serif;
    position: relative;
  }
  .card {
    position: absolute;
    top: 246px;
    width: 540px;
    height: 309px;
    border-radius: 14px;
    border-bottom: 3px solid var(--orange);
    overflow: hidden;
    box-shadow: 0 10px 24px rgba(0,0,0,.18);
  }
  .card--back { left: 40px; background: var(--navy); }
  .card--front { left: 620px; background: var(--white); }

  .brand {
    display: flex;
    align-items: center;
    gap: 10px;
    font-weight: 700;
    white-space: nowrap;
  }
  .brand__dot { border-radius: 50%; background: var(--orange); flex: none; }
  .card--back .brand {
    position: absolute; left: 50%; top: 50%;
    transform: translate(-50%, -50%);
    font-size: 38px; color: var(--white);
  }
  .card--back .brand__dot { width: 26px; height: 26px; }
  .card--front .brand {
    position: absolute; left: 22px; top: 122px;
    font-size: 22px; color: var(--navy);
  }
  .card--front .brand__dot { width: 16px; height: 16px; }

  .divider {
    position: absolute; left: 228px; top: 58px;
    width: 1.5px; height: 150px; background: var(--navy);
  }
  .contact { position: absolute; left: 246px; top: 44px; color: var(--ink); z-index: 1; }
  .contact__name { font-size: 22px; font-weight: 700; letter-spacing: -.3px; }
  .contact__role { font-size: 12.5px; color: var(--orange); margin: 2px 0 7px; }
  .contact__address { font-size: 12px; line-height: 1.35; margin-bottom: 5px; }
  .contact__list { list-style: none; font-size: 12px; line-height: 1.5; }
  .contact__list li { display: flex; align-items: center; gap: 7px; }
  .contact__list svg { width: 11px; height: 11px; flex: none; }

  .wave { position: absolute; inset: 0; width: 540px; height: 309px; }
  .social { position: absolute; top: 198px; right: 16px; display: flex; gap: 6px; }
  .social span { width: 22px; height: 22px; border-radius: 50%; background: var(--orange); }
</style>
</head>
<body>
  <section class="card card--back" aria-label="Card back">
    <div class="brand"><span class="brand__dot"></span>Lanternfield HR</div>
  </section>

  <section class="card card--front" aria-label="Card front">
    <svg class="wave" viewBox="0 0 540 309" aria-hidden="true">
      <path d="M0,284 C180,274 340,258 436,226 C494,196 520,130 540,98" fill="none" stroke="var(--orange)" stroke-width="3"/>
      <path d="M0,309 L0,296 C185,286 345,270 440,238 C494,208 522,142 540,112 L540,309 Z" fill="var(--navy)"/>
    </svg>

    <div class="brand"><span class="brand__dot"></span>Lanternfield HR</div>
    <div class="divider"></div>

    <div class="contact">
      <div class="contact__name">Dana Whitford</div>
      <div class="contact__role">Manager</div>
      <div class="contact__address">4827 Millbrook Ave Suite 230<br>Cleveland, Ohio 44987</div>
      <ul class="contact__list">
        <li><svg viewBox="0 0 12 12"><path d="M2.5 1 L4.5 1 L5.3 3.6 L4 4.6 C4.6 6 5.9 7.3 7.4 8 L8.4 6.7 L11 7.5 L11 9.5 C11 10.3 10.3 11 9.5 11 C5 11 1 7 1 2.5 C1 1.7 1.7 1 2.5 1Z" fill="var(--orange)"/></svg>216-555-0143</li>
        <li><svg viewBox="0 0 12 12"><rect x="3" y="0.5" width="6" height="11" rx="1" fill="none" stroke="var(--orange)" stroke-width="1.3"/></svg>216-555-0192</li>
        <li><svg viewBox="0 0 12 12"><rect x="0.5" y="2.5" width="11" height="7" fill="var(--orange)"/><path d="M0.5 2.5 L6 6.5 L11.5 2.5" fill="none" stroke="#fff" stroke-width="1"/></svg>info@lanternfieldhr.example</li>
        <li><svg viewBox="0 0 12 12"><circle cx="6" cy="6" r="5" fill="none" stroke="var(--orange)" stroke-width="1.3"/><path d="M1 6 H11 M6 1 C3.5 4 3.5 8 6 11 M6 1 C8.5 4 8.5 8 6 11" fill="none" stroke="var(--orange)" stroke-width="1"/></svg>www.lanternfieldhr.example</li>
      </ul>
    </div>

    <div class="social" aria-label="Social profiles"><span></span><span></span></div>
  </section>
</body>
</html>
```